Brenwick's Summit Concrete Services

Concrete, foundations, driveways, decks, pool coping, color concrete, stamp concrete
Pavers,
I would like to see someone finishing concrete(logo)
I would like to see a card with a background showing a nice color driveway
On one side the contact info with the lic# and on the other side what my company does
But in both sides the name of mycompany

Reason: I would like to see a logo (one where theres someone finishing concrete)

Hello, to everyone i just want a say thanks for helping me design my business cards and or logo for my company. I like your desigms but i am not completly satisfy. Design #2326 last four digits has the right idea.. I i would like to see someone on their knees finishing concrete. My company is small, im just starting. I want a strong design and or logo so that when people see mycards can tell right away that im profesional.

Industry/Entity Type

Concrete

Contact Information for Business Card

Rolando 555 3817042
Tavo 555 6490318
Lic #2958164
bsconcreteservices@mailvesta.example

```html
<!DOCTYPE html>
<html lang="en">
<head>
<meta charset="utf-8">
<title>Brenwick's Summit Concrete Services — Business Card</title>
<link href="https://fonts.googleapis.com/css2?family=Lato:wght@300;400;700;900&display=swap" rel="stylesheet">
<style>
  :root {
    --page-bg: #ecebe8;
    --card-dark: #2b2b2d;
    --card-dark-line: #3a3a3d;
    --brand-red: #c01c2b;
    --ink-light: #ffffff;
    --ink-muted: #c9c9c9;
    --ink-dark: #2a2a2a;
    --paper: #f1f1f1;
    --water-deep: #1d5fa6;
    --water-light: #5aa6dc;
    --stone-light: #c9c9c7;
    --stone-mid: #9d9d9b;
  }
  * { box-sizing: border-box; margin: 0; padding: 0; }
  html, body {
    width: 1200px; height: 900px; overflow: hidden;
    background: var(--page-bg);
    font-family: "Lato", Arial, sans-serif;
  }
  .canvas { position: relative; width: 1200px; height: 900px; }
  .card {
    position: absolute; width: 525px; height: 300px; overflow: hidden;
    box-shadow: 0 10px 30px rgba(0,0,0,.22);
  }

  /* Front */
  .card-front { left: 110px; top: 110px; }
  .front-photo {
    position: absolute; inset: 0;
    background:
      radial-gradient(ellipse 300px 95px at 340px 35px, var(--water-light) 0%, var(--water-deep) 82%, #6f7f8c 86%, var(--stone-mid) 92%, transparent 93%),
      linear-gradient(160deg, var(--stone-light), var(--stone-mid));
  }
  .front-band { position: absolute; inset: 0; }
  .front-brand {
    position: absolute; left: 60px; top: 150px;
    display: flex; align-items: center; gap: 16px;
  }
  .brand-square { width: 58px; height: 58px; background: var(--brand-red); flex: none; }
  .front-name {
    position: absolute; left: 250px; top: 112px;
    transform: rotate(-8.6deg); transform-origin: left top;
    color: var(--ink-light);
  }
  .front-name .name-main { font-weight: 900; font-size: 27px; line-height: 1; }
  .front-name .name-sub { font-weight: 300; font-size: 22px; line-height: 1.1; }
  .front-mark-name {
    position: absolute; left: 60px; top: 232px;
    color: var(--brand-red); font-weight: 900; font-size: 15px;
    transform: rotate(-8.6deg); transform-origin: left top;
  }

  /* Back */
  .card-back { left: 565px; top: 480px; background: var(--paper); }
  .back-panel { position: absolute; inset: 0; }
  .contact {
    position: absolute; left: 48px; width: 200px;
    color: var(--ink-light);
  }
  .contact-name { font-weight: 900; font-size: 23px; }
  .contact-phone { font-weight: 400; font-size: 15px; color: var(--ink-muted); margin-top: 10px; letter-spacing: .5px; }
  .contact-rule { height: 1px; background: var(--card-dark-line); margin-top: 12px; width: 180px; }
  .phone-tab {
    position: absolute; width: 38px; height: 30px; background: var(--brand-red);
    display: flex; align-items: center; justify-content: center;
  }
  .contact-one { top: 60px; }
  .contact-two { top: 165px; }
  .tab-one { left: 232px; top: 66px; }
  .tab-two { left: 262px; top: 168px; }
  .back-brand {
    position: absolute; left: 345px; top: 55px; width: 160px;
    display: flex; flex-direction: column; align-items: center; text-align: center;
  }
  .back-brand .brand-square { width: 64px; height: 64px; }
  .back-brand-name {
    margin-top: 14px; color: var(--brand-red); font-weight: 900; font-size: 17px; line-height: 1.15;
  }
  .license { margin-top: 14px; color: var(--ink-dark); font-weight: 900; font-size: 17px; }
</style>
</head>
<body>
<main class="canvas">

  <section class="card card-front" aria-label="Business card front">
    <div class="front-photo" role="img" aria-label="Photo of a blue swimming pool edged with stamped grey concrete pavers"></div>
    <svg class="front-band" width="525" height="300" viewBox="0 0 525 300" aria-hidden="true">
      <polygon points="0,160 525,78 525,190 0,272" fill="var(--card-dark)"/>
    </svg>
    <div class="front-brand">
      <div class="brand-square"></div>
    </div>
    <div class="front-name">
      <div class="name-main">Brenwick's Summit</div>
      <div class="name-sub">Concrete Services</div>
    </div>
    <div class="front-mark-name">Brenwick's Summit</div>
  </section>

  <section class="card card-back" aria-label="Business card back">
    <svg class="back-panel" width="525" height="300" viewBox="0 0 525 300" aria-hidden="true">
      <polygon points="0,0 178,0 338,300 0,300" fill="var(--card-dark)"/>
    </svg>

    <div class="contact contact-one">
      <div class="contact-name">Tavo</div>
      <div class="contact-phone">555 6490318</div>
      <div class="contact-rule"></div>
    </div>
    <div class="phone-tab tab-one" aria-hidden="true">
      <svg width="18" height="14" viewBox="0 0 18 14"><path d="M1 4c3-3 13-3 16 0l-1 3-4-1V4H6v2L2 7z M4 8h10l2 5H2z" fill="#fff"/></svg>
    </div>

    <div class="contact contact-two">
      <div class="contact-name">Rolando</div>
      <div class="contact-phone">555 3817042</div>
      <div class="contact-rule"></div>
    </div>
    <div class="phone-tab tab-two" aria-hidden="true">
      <svg width="18" height="14" viewBox="0 0 18 14"><path d="M1 4c3-3 13-3 16 0l-1 3-4-1V4H6v2L2 7z M4 8h10l2 5H2z" fill="#fff"/></svg>
    </div>

    <div class="back-brand">
      <div class="brand-square"></div>
      <div class="back-brand-name">Brenwick's Summit</div>
      <div class="license">Lic #2958164</div>
    </div>
  </section>

</main>
</body>
</html>
```